Civora - a Political Plebescite app.

There is a current app in the App Store (worldwide) and Play Store (worldwide) called yourTally (with an owl logo). The UX needs to be redesigned to make it more visually pleasing.

The requirement is to build a UX that is suitable for both iOS and Android - i.e. consistent look for both platforms. The design is to span the variety of sizes available from smart devices - phones and tablets. The layout as it stands is portrait only, and a secondary design to encompass landscape is wanted.

You would need to download the app to get a feel for all the functionality - there are 3 visible forms (currently) and a hidden form, that will be used in the near future - this hidden form will look similar to the main (first) form.

To get full functionality you need to do the following:
Go to the Options page
Toggle the top slide
Click on UNREGISTERED
Select a state/territory

I know this is a bit non-intuitive - in the "real" product these steps are automated - but for this release the user gets to choose.

Once this is done - the other button(s) appear in the top left of the screen - and data is available to be displayed.

The current forms are included in this brief. The Options screen will ultimately not be showing all the current data, only the lower slider (or other indicator) and the associated version and copyright notices. The hidden screen is much like the main screen - showing the name of the bill and information pertaining to that bill - there needs to be a button (or action site) to toggle between the main and this hidden screen.

Target Market(s)

All eligable voters (currently in Australia)

Industry/Entity Type

Political

Requirements
Should not have
• Do not present to me my own/existing design with the only change being colours and label layout.

```html
<!DOCTYPE html>
<html lang="en">
<head>
<meta charset="utf-8">
<title>Civora – General</title>
<link rel="stylesheet" href="https://fonts.googleapis.com/css2?family=Roboto:wght@300;400&display=swap">
<style>
  :root {
    --navy: #1f2f47;
    --white: #ffffff;
    --tab-bg: #f2f2f2;
    --tab-text: #5a5a5a;
    --divider: #d6d6d6;
    --accent-green: #3f7a60;
    --body-text: #6a6a6a;
    --gear-blue: #1c86dc;
    --map-green: #4a8a6c;
    --map-red: #a63222;
    --status-green: #1a8f2a;
  }
  * { box-sizing: border-box; margin: 0; padding: 0; }
  html, body { width: 674px; height: 1200px; overflow: hidden; background: var(--white); }
  body { font-family: "Roboto", sans-serif; position: relative; }

  .status-bar {
    height: 42px; background: var(--navy); color: var(--white);
    position: relative; font-weight: 300; font-size: 22px;
  }
  .status-bar .carrier { position: absolute; left: 13px; top: 8px; display: flex; align-items: center; gap: 6px; }
  .signal { display: flex; gap: 3px; }
  .signal span { width: 11px; height: 11px; border-radius: 50%; border: 1.5px solid var(--white); }
  .signal span.on { background: var(--white); }
  .status-bar .time { position: absolute; left: 0; right: 0; top: 7px; text-align: center; font-weight: 400; font-size: 24px; }
  .status-bar .right { position: absolute; right: 12px; top: 8px; display: flex; align-items: center; gap: 10px; }
  .battery { width: 48px; height: 20px; border: 2px solid var(--white); border-radius: 4px; padding: 2px; position: relative; }
  .battery::after { content: ""; position: absolute; right: -5px; top: 5px; width: 3px; height: 7px; background: var(--white); border-radius: 0 2px 2px 0; }
  .battery i { display: block; height: 100%; background: var(--white); border-radius: 1px; }

  .nav-bar { height: 89px; background: var(--navy); position: relative; }
  .region-switch { position: absolute; left: 19px; top: 30px; display: flex; gap: 12px; }
  .region-switch .region { width: 40px; height: 36px; border-radius: 4px; }
  .region.green { background: var(--map-green); }
  .region.red { background: var(--map-red); }
  .nav-bar .title { position: absolute; left: 0; right: 0; top: 28px; text-align: center; color: var(--white); font-size: 29px; font-weight: 400; }
  .nav-actions { position: absolute; right: 18px; top: 34px; display: flex; gap: 20px; align-items: center; }

  .tabs { height: 62px; background: var(--tab-bg); display: flex; position: relative; }
  .tab { flex: 1; display: flex; align-items: center; justify-content: center; font-size: 23px; color: var(--tab-text); position: relative; }
  .tab + .tab::before { content: ""; position: absolute; left: 0; top: 9px; height: 42px; width: 1px; background: var(--divider); }
  .tab.active { color: var(--accent-green); }
  .tab.active::after { content: ""; position: absolute; left: 0; right: 0; bottom: 0; height: 2px; background: var(--accent-green); }

  .content { padding: 20px 19px 0; color: var(--body-text); font-weight: 300; font-size: 17.9px; line-height: 26.2px; white-space: nowrap; }
  .content p + p { margin-top: 26.2px; }

  .footer-bar { position: absolute; left: 0; right: 0; bottom: 0; height: 40px; background: var(--navy); color: var(--white); font-size: 19px; font-weight: 300; }
  .footer-bar .live-dot { position: absolute; left: 19px; top: 11px; width: 18px; height: 18px; border-radius: 50%; background: var(--status-green); }
  .footer-bar .chamber { position: absolute; left: 0; right: 0; top: 9px; text-align: center; }
  .footer-bar .count { position: absolute; right: 18px; top: 9px; }
</style>
</head>
<body>
  <div class="status-bar">
    <div class="carrier">
      <div class="signal"><span class="on"></span><span class="on"></span><span class="on"></span><span></span><span></span></div>
      <span>VOLTA</span>
      <svg width="24" height="18" viewBox="0 0 24 18"><path d="M2 6a14 14 0 0 1 20 0M5.5 9.5a9 9 0 0 1 13 0M9 13a4 4 0 0 1 6 0" fill="none" stroke="#fff" stroke-width="2.4" stroke-linecap="round"/><circle cx="12" cy="16" r="1.8" fill="#fff"/></svg>
    </div>
    <div class="time">4:21 PM</div>
    <div class="right">
      <svg width="14" height="24" viewBox="0 0 14 24"><path d="M2 7l10 10-5 5V2l5 5L2 17" fill="none" stroke="#8a93a3" stroke-width="1.6"/></svg>
      <span>100%</span>
      <div class="battery"><i></i></div>
    </div>
  </div>

  <header class="nav-bar">
    <div class="region-switch">
      <div class="region green" role="img" aria-label="Map of New South Wales, selected region"></div>
      <div class="region red" role="img" aria-label="Map of New South Wales, alternate chamber"></div>
      <div class="region green" role="img" aria-label="Map of Australia, federal"></div>
      <div class="region red" role="img" aria-label="Map of Australia, alternate chamber"></div>
    </div>
    <h1 class="title">Title</h1>
    <div class="nav-actions">
      <svg width="33" height="33" viewBox="0 0 33 33" aria-label="Help"><circle cx="16.5" cy="16.5" r="16" fill="#fff"/><path d="M12 13a4.5 4.5 0 1 1 6.5 4c-1.4.7-2 1.4-2 3v1" fill="none" stroke="#1f2f47" stroke-width="3" stroke-linecap="round"/><circle cx="16.5" cy="25.5" r="1.9" fill="#1f2f47"/></svg>
      <svg width="34" height="34" viewBox="0 0 34 34" aria-label="Settings"><g fill="#1c86dc" transform="translate(17 17)"><rect x="-4" y="-17" width="8" height="34" rx="1.5"/><rect x="-4" y="-17" width="8" height="34" rx="1.5" transform="rotate(45)"/><rect x="-4" y="-17" width="8" height="34" rx="1.5" transform="rotate(90)"/><rect x="-4" y="-17" width="8" height="34" rx="1.5" transform="rotate(135)"/><circle r="12"/></g><circle cx="17" cy="17" r="5" fill="#1f2f47"/></svg>
    </div>
  </header>

  <nav class="tabs">
    <div class="tab active">GENERAL</div>
    <div class="tab">FAQ</div>
    <div class="tab">CONTACT</div>
  </nav>

  <main class="content">
    <p>Lorem ipsum dolor sit amet, consectetur adipiscing elit.</p>
    <p>Nam condimentum leo sed nisi malesuada, sed accumsan metus ultricies.<br>
    Donec eleifend nibh in ultrices tempus. Morbi id tempor lorem. Suspendisse po-<br>
    tenti. Fusce at augue pulvinar, ultricies nisl id, bibendum est. Cras semper ac<br>
    nulla ut vulputate. Nam faucibus sagittis odio, quis molestie elit sollicitudin et.<br>
    Nam dapibus fringilla orci, quis efficitur leo consectetur eu. Vivamus dui lectus,<br>
    mollis a condimentum consequat, ullamcorper porta lectus. Vivamus sit amet<br>
    justo enim. Donec nec lorem mi. Lorem ipsum dolor sit amet, consectetur adipi-<br>
    scing elit.</p>
    <p>Nam condimentum leo sed nisi malesuada, sed accumsan metus ultricies.<br>
    Donec eleifend nibh in ultrices tempus. Morbi id tempor lorem. Suspendisse po-<br>
    tenti. Fusce at augue pulvinar, ultricies nisl id, bibendum est. Cras semper ac<br>
    nulla ut vulputate. Nam faucibus sagittis odio, quis molestie elit sollicitudin et.<br>
    Nam dapibus fringilla orci, quis efficitur leo consectetur eu. Vivamus dui lectus,<br>
    mollis a condimentum consequat, ullamcorper porta lectus. Vivamus sit amet<br>
    justo enim. Donec nec lorem mi. Lorem ipsum dolor sit amet, consectetur adipi-<br>
    scing elit.</p>
    <p>Nam condimentum leo sed nisi malesuada, sed accumsan metus ultricies.<br>
    Donec eleifend nibh in ultrices tempus. Morbi id tempor lorem. Suspendisse po-<br>
    tenti. Fusce at augue pulvinar, ultricies nisl id, bibendum est. Cras semper ac<br>
    nulla ut vulputate. Nam faucibus sagittis odio, quis molestie elit sollicitudin et.<br>
    Nam dapibus fringilla orci, quis efficitur leo consectetur eu. Vivamus dui lectus,<br>
    mollis a condimentum consequat, ullamcorper porta lectus.</p>
  </main>

  <footer class="footer-bar">
    <span class="live-dot"></span>
    <span class="chamber">Legislative Council</span>
    <span class="count">1 / 77</span>
  </footer>
</body>
</html>
```